Business card design for QuelMarvion

I need a business card based on the logo design produced for QuelMarvion. The company is focused on triathlon and endurance sport coaching and the tag line is (per the logo) "Endurance. Resilience. Achievement". The design should be sophisticated, appropriate to an affluent and business oriented target market. Colors are optional but the color of the logo probably dictates the color used on the card. I envisage using the red logo, with black print for the wording and contact numbers on a white or cream background, but am open to alternative suggestions. I expect to select something fairly conventional, but would like to see some designs that are less conventional to stretch my thinking on what could be appropriate. I am assuming a single side design is best, but willing to consider double sided as an option.

Target Market(s)

Individual athletes and corporate health and wellness leaders

Industry/Entity Type

Health And Wellness

Contact Information for Business Card

The card should provide the following information:
Logo
My name: Gordon Lashby
Company website: QuelMarvion.com
My email: gordon.lashby@quelmarvion.com
My cell phone number: +1-555-018-2739

Font styles to use
Sans Serif

Colors

Designer to choose colors to be used in the design.

Requirements
Must have
• Space on the card - simple design, not over crowded.
Nice to have
• clean and clear font, nothing garish or mass market like
Should not have
• Do not add pictures

```html
<!DOCTYPE html>
<html lang="en">
<head>
<meta charset="utf-8">
<title>QuelMarvion — Business Card</title>
<link href="https://fonts.googleapis.com/css2?family=Roboto:wght@400;500;700&family=Roboto+Condensed:wght@700&display=swap" rel="stylesheet">
<style>
  :root {
    --backdrop: #2a2a2b;
    --card-white: #f4f4f4;
    --card-black: #0b0b0c;
    --brand-red: #b3262b;
    --ink: #141414;
    --ink-soft: #555558;
    --rule: #8a8a8a;
    --paper-white: #ffffff;
  }
  html, body {
    margin: 0;
    width: 1200px;
    height: 960px;
    overflow: hidden;
    background: var(--backdrop);
    font-family: "Roboto", Arial, sans-serif;
  }
  .canvas { position: relative; width: 1200px; height: 960px; }

  /* Front */
  .card-front {
    position: absolute; left: 314px; top: 113px;
    width: 600px; height: 342px;
    background: var(--card-white);
    overflow: hidden;
  }
  .brand {
    position: absolute; right: 35px; top: 72px;
  }
  .brand-name {
    display: flex; align-items: center; justify-content: flex-end; gap: 8px;
    font-family: "Roboto", Arial, sans-serif;
    font-weight: 700; font-size: 31px; line-height: 1;
    color: var(--brand-red); letter-spacing: -0.3px;
  }
  .brand-dot {
    width: 12px; height: 12px; border-radius: 50%;
    background: var(--brand-red);
  }
  .holder { position: absolute; left: 34px; top: 217px; }
  .holder-name {
    font-family: "Roboto Condensed", "Arial Narrow", sans-serif;
    font-weight: 700; font-size: 21px; color: var(--brand-red);
    line-height: 1;
  }
  .holder-role {
    margin-top: 4px;
    font-weight: 500; font-size: 14.5px; color: var(--ink);
    letter-spacing: 0.3px;
  }
  .divider {
    position: absolute; left: 34px; right: 35px; top: 266px;
    height: 1px; background: var(--rule);
  }
  .contacts {
    position: absolute; left: 34px; top: 278px;
    list-style: none; margin: 0; padding: 0;
    font-size: 14.5px; color: var(--ink-soft);
  }
  .contacts li { display: flex; align-items: center; gap: 9px; height: 20px; }
  .contacts svg { width: 13px; height: 13px; flex: none; }
  .website-front {
    position: absolute; right: 35px; top: 301px;
    font-weight: 500; font-size: 14px; color: var(--brand-red);
  }
  .edge-band {
    position: absolute; left: 0; bottom: 0; width: 600px; height: 9px;
  }

  /* Back */
  .card-back {
    position: absolute; left: 311px; top: 472px;
    width: 600px; height: 343px;
    background: var(--card-black);
  }
  .back-brand {
    position: absolute; left: 0; right: 0; top: 142px;
    display: flex; align-items: center; justify-content: center; gap: 14px;
    font-weight: 700; font-size: 46px; line-height: 1;
    color: var(--brand-red);
  }
  .back-brand .brand-dot { width: 18px; height: 18px; }
  .website-back {
    position: absolute; left: 0; right: 0; top: 295px;
    text-align: center;
    font-size: 14px; letter-spacing: 2.6px; color: var(--paper-white);
  }
</style>
</head>
<body>
<main class="canvas">

  <section class="card-front" aria-label="Business card front">
    <div class="brand">
      <div class="brand-name"><span class="brand-dot"></span>QuelMarvion</div>
    </div>

    <div class="holder">
      <div class="holder-name">GORDON LASHBY</div>
      <div class="holder-role">TRIATHLETE</div>
    </div>

    <div class="divider"></div>

    <ul class="contacts">
      <li>
        <svg viewBox="0 0 13 13" aria-hidden="true">
          <rect x="3" y="0.5" width="7" height="12" rx="1.2" fill="none" stroke="var(--brand-red)" stroke-width="1.4"/>
          <rect x="5" y="10" width="3" height="1" fill="var(--brand-red)"/>
        </svg>
        +1-555-018-2739
      </li>
      <li>
        <svg viewBox="0 0 13 13" aria-hidden="true">
          <rect x="0.5" y="2.5" width="12" height="8" fill="var(--brand-red)"/>
          <path d="M0.8 2.8 L6.5 7 L12.2 2.8" fill="none" stroke="var(--card-white)" stroke-width="1"/>
        </svg>
        gordon.lashby@quelmarvion.com
      </li>
    </ul>

    <div class="website-front">www.QuelMarvion.com</div>

    <svg class="edge-band" viewBox="0 0 600 9" preserveAspectRatio="none" aria-hidden="true">
      <rect x="0" y="0" width="600" height="9" fill="var(--card-black)"/>
      <polygon points="0,0 334,0 330,9 0,9" fill="var(--brand-red)"/>
      <polygon points="334,0 338,0 334,9 330,9" fill="var(--paper-white)"/>
    </svg>
  </section>

  <section class="card-back" aria-label="Business card back">
    <div class="back-brand"><span class="brand-dot"></span>QuelMarvion</div>
    <div class="website-back">www.QuelMarvion.com</div>
  </section>

</main>
</body>
</html>
```